Webbanner-Design für Beratungs-, Ausbildungs- und Forschungsunternehmen
Sehr schnelle Erstellung und Anpassung des Designs. Sehr gute Arbeit!
Zielgruppe
Wir sind ein Beratungs-, Ausbildungs- und Forschungsunternehmen im Bereich der chemischen instrumentellen Analytik.
Unsere Zielgruppe sind andere Unternehmen in unserem Bereich, deren Mitarbeiter*Innen, sowie Hochschulen und Wissenschaftler.
Für eine wissenschaftliche Veranstaltung suchen wir ein Banner, das die Sichtbarkeit der Veranstaltung im Vorfeld erhöhen soll.
Aufgabenstellung
Das Webbanner soltle alle wichtigen Informationen zur Veranstaltung, sowie unser Firmenlogo enthalten (Titel, Datum, Ort, Hinweis auf mögliche Online-Teilnahme)
Ein schlichtes Design wäre wünschenswert, es darf aber gerne auffallen. Das Banner soll zur Bewerbung der Veranstaltung auf Websiten und in den sozialen Medien genutzt werden
Die Größe soll W:768 x H:90 px sein. (mit Hyperlink)

```html
<!DOCTYPE html>
<html lang="en">
<head>
<meta charset="utf-8">
<title>GC Meets NTS – Web Banner</title>
<link href="https://fonts.googleapis.com/css2?family=Poppins:wght@400;600;700&display=swap" rel="stylesheet">
<style>
  :root {
    --stage-grey: #9b9b9b;
    --label-grey: #767676;
    --banner-cyan: #5bd3d4;
    --banner-white: #ffffff;
    --ink: #1d1d1f;
  }
  * { margin: 0; padding: 0; box-sizing: border-box; }
  html, body {
    width: 1200px;
    height: 360px;
    overflow: hidden;
    background: var(--stage-grey);
    font-family: "Poppins", sans-serif;
    color: var(--ink);
  }
  .stage { position: relative; width: 1200px; height: 360px; }
  .banner {
    position: absolute;
    left: 140px;
    top: 126px;
    width: 922px;
    height: 108px;
    display: block;
    text-decoration: none;
    color: var(--ink);
  }
  .banner-shapes { position: absolute; inset: 0; }
  .brand-name {
    position: absolute;
    left: 0;
    top: 0;
    width: 205px;
    height: 108px;
    display: flex;
    align-items: center;
    justify-content: center;
    gap: 8px;
    font-weight: 700;
    font-size: 22px;
    letter-spacing: 1px;
  }
  .brand-dot {
    width: 12px; height: 12px; border-radius: 50%;
    background: var(--banner-cyan);
  }
  .event-title {
    position: absolute;
    left: 234px;
    top: 10px;
    font-weight: 700;
    font-size: 26px;
    line-height: 1.3;
  }
  .event-subtitle {
    position: absolute;
    left: 234px;
    top: 44px;
    font-weight: 400;
    font-size: 15.5px;
    line-height: 1.3;
  }
  .event-location {
    position: absolute;
    left: 234px;
    top: 64px;
    font-weight: 600;
    font-size: 18px;
    line-height: 1.3;
  }
  .event-date-icon { position: absolute; left: 695px; top: 46px; }
  .event-dates {
    position: absolute;
    left: 742px;
    top: 33px;
    font-weight: 600;
    font-size: 18px;
    line-height: 1.4;
  }
  .format-label {
    position: absolute;
    left: 0;
    width: 1200px;
    top: 288px;
    text-align: center;
    font-weight: 700;
    font-size: 31px;
    color: var(--label-grey);
  }
</style>
</head>
<body>
<div class="stage">
  <a class="banner" href="#">
    <svg class="banner-shapes" width="922" height="108" viewBox="0 0 922 108">
      <rect width="922" height="108" fill="var(--banner-cyan)"/>
      <polygon points="0,0 220,0 174,108 0,108" fill="var(--banner-white)"/>
      <polygon points="214,0 222,0 176,108 168,108" fill="var(--ink)"/>
    </svg>
    <div class="brand-name"><span class="brand-dot"></span>KROMALAB</div>
    <div class="event-title">GC MEETS NTS</div>
    <div class="event-subtitle">Gas Chromatography meets Non-Target Screening</div>
    <div class="event-location">IN AUGSBURG, GERMANY AND ONLINE</div>
    <svg class="event-date-icon" width="34" height="36" viewBox="0 0 34 36" aria-hidden="true">
      <circle cx="13" cy="22" r="10" fill="none" stroke="var(--ink)" stroke-width="3.4"/>
      <line x1="20" y1="15" x2="30" y2="5" stroke="var(--ink)" stroke-width="3.4" stroke-linecap="round"/>
      <polyline points="21,4 31,4 31,14" fill="none" stroke="var(--ink)" stroke-width="3.4" stroke-linejoin="round"/>
    </svg>
    <div class="event-dates">04.02.2021 and<br>05.02.2021</div>
  </a>
  <div class="format-label">W:768 X H:90 PX</div>
</div>
</body>
</html>
```